Flyer for teen fitness class at a physiotherapy clinic

We are a passionate Physiotherapy Clinic requiring a flyer to promote our new service a fitness class for teenagers, which is called Youth's FLX - Flexible Limber Xtra Power. The aim of the class is to prevents injuries in sports, improve sporting performance and provide safe activity for otherwise inactive teens. The aim of the flyer is to make people aware of this new service and interested in joining. Ideally the Flyer would incorporate blue colours. Our logo must be on the flier, and at least one or two of the photos provided. Our logo is provided in the attachments. Required information : Youth's FLX: Flexible Limber Xtra Power, times Mondays and Wednesdays 4 -5. Can be claimed on private health insurance. Expert advice to tailor a program to individual needs. For more information go www.rmpvq.com.au or phone 03)5871 6093.

Industry/Entity Type

Clinic

```html
<!DOCTYPE html>
<html lang="en">
<head>
<meta charset="utf-8">
<title>Youth's FLX Flyer</title>
<link rel="stylesheet" href="https://fonts.googleapis.com/css2?family=Didact+Gothic&family=Montserrat:wght@600;700;800&display=swap">
<style>
  :root {
    --blue-mid: #3c6a9b;
    --blue-deep: #1f4670;
    --blue-light: #5585b8;
    --ink: #111111;
    --paper-top: #d6d6d6;
    --paper-bottom: #f7f7f7;
    --white: #ffffff;
  }
  * { margin: 0; padding: 0; box-sizing: border-box; }
  html, body { width: 1200px; height: 850px; overflow: hidden; }
  body { background: var(--paper-bottom); }
  .flyer {
    position: relative;
    width: 1200px;
    height: 850px;
    overflow: hidden;
    background: linear-gradient(180deg, var(--paper-top) 0%, #e6e6e6 45%, var(--paper-bottom) 100%);
    color: var(--ink);
    font-family: "Didact Gothic", "Century Gothic", sans-serif;
  }
  .bands { position: absolute; inset: 0; }
  .brand {
    position: absolute;
    left: 24px;
    top: 46px;
    display: flex;
    align-items: center;
    gap: 12px;
  }
  .brand-dot {
    width: 34px; height: 34px;
    border-radius: 50%;
    background: var(--white);
  }
  .brand-name {
    font-family: "Montserrat", sans-serif;
    font-weight: 700;
    font-size: 20px;
    line-height: 1.15;
    color: var(--white);
  }
  .headline {
    position: absolute;
    left: 120px;
    top: 176px;
    width: 1040px;
    font-family: "Montserrat", sans-serif;
    font-weight: 800;
    font-size: 70px;
    line-height: 1;
    letter-spacing: 0;
    white-space: nowrap;
  }
  .intro {
    position: absolute;
    left: 0; right: 0;
    top: 334px;
    text-align: center;
    font-size: 52px;
    line-height: 64px;
    word-spacing: 4px;
    white-space: nowrap;
  }
  .intro strong {
    font-family: "Montserrat", sans-serif;
    font-weight: 700;
    font-size: 48px;
  }
  .details { position: absolute; left: 48px; top: 546px; list-style: none; }
  .detail {
    display: flex;
    align-items: center;
    height: 69px;
    font-size: 28px;
    word-spacing: 3px;
    white-space: nowrap;
  }
  .detail svg { width: 42px; height: 42px; margin-right: 22px; flex: none; }
  .hashtag {
    position: absolute;
    right: 6px;
    bottom: 8px;
    font-family: "Montserrat", sans-serif;
    font-weight: 800;
    font-size: 58px;
    line-height: 1;
    color: var(--white);
    white-space: nowrap;
  }
</style>
</head>
<body>
<main class="flyer">
  <svg class="bands" width="1200" height="850" viewBox="0 0 1200 850" aria-hidden="true">
    <polygon points="0,0 1200,0 1200,6 0,200" fill="var(--blue-deep)"/>
    <polygon points="0,0 1185,0 0,170" fill="var(--blue-mid)"/>
    <polygon points="0,0 1140,0 0,150" fill="var(--blue-light)" opacity="0.35"/>
    <polygon points="0,850 1200,850 1200,724 0,846" fill="var(--blue-deep)"/>
    <polygon points="0,850 1200,850 1200,746" fill="var(--blue-mid)"/>
  </svg>

  <div class="brand">
    <span class="brand-dot"></span>
    <span class="brand-name">Kestrel Cove<br>Sports Clinic</span>
  </div>

  <h1 class="headline">INTERESTED IN JOGGING ?</h1>

  <p class="intro"><strong>JOIN</strong> AT OUR NEW SERVICE:<br>YOUTH'S FLX - FLEXIBLE LIMBER XTRA POWER</p>

  <ul class="details">
    <li class="detail">
      <svg viewBox="0 0 42 42" aria-hidden="true"><path d="M4 6 L4 18 L24 38 L38 24 L18 4 L6 4 Z" fill="none" stroke="var(--ink)" stroke-width="2.5" stroke-linejoin="round"/><circle cx="11" cy="11" r="2.6" fill="none" stroke="var(--ink)" stroke-width="2"/></svg>
      YOUTH'S FLX: FLEXIBLE LIMBER XTRA POWER
    </li>
    <li class="detail">
      <svg viewBox="0 0 42 42" aria-hidden="true"><circle cx="21" cy="21" r="16" fill="none" stroke="var(--ink)" stroke-width="3.5"/><path d="M18 12 V24 H27" fill="none" stroke="var(--ink)" stroke-width="3.5"/></svg>
      MONDAYS AND WEDNESDAYS 4 - 5 PM
    </li>
    <li class="detail">
      <svg viewBox="0 0 42 42" aria-hidden="true"><path d="M21 3 A16 16 0 1 1 20.9 3 Z M21 35 L16 34 L21 41 L26 34 Z" fill="var(--ink)"/><circle cx="21" cy="12" r="2.6" fill="var(--white)"/><rect x="18.5" y="17" width="5" height="13" fill="var(--white)"/></svg>
      WWW.RMPVQ.COM.AU/PHONE (03)5871 6093
    </li>
  </ul>

  <p class="hashtag">#YOUTHFLX</p>
</main>
</body>
</html>
```